New Design for Poker Card Box

Looking for someone to design a Poker Card Box for my newly design Poker Cards. The box has to new and modem, I'm open to suggestions, the end product should be unique and amazing enough that people would want to buy this deck of cards.
The gold trim on the sample box attached will be printed in gold foil and must be produced as a separate layer for easier printing. THIS IS ESSENTIAL.
- My logo on the box is essential
- The writing on the bottom flap 'Copyright 2021 Cobalt Ember Studios, Marlow Bay, Westerland, Printed by RWLT'. should also be there.
- The words Playing Cards and Premium Edition should also be there.
- My website is www.cobaltember.com.au you can also use the banner from my home page if need be.
- I like the Vegas header I have with the Kelverin Arch and Moss Pavilion in the background, if I can get a few designs with these visible that would be good.
- I tried to attach the images of the face of the cards but the file is 8.8MB and wouldn't load. I can maybe get these to you somehow if need be.

Please feel free to message if I've missed anything or if you have any questions.

Rod

Target Market(s)

Poker enthusiasts, Poker Card collectors, mainly US market

Requirements
Must have
• All must haves are noted in the Project Description.

```html
<!DOCTYPE html>
<html lang="en">
<head>
<meta charset="utf-8">
<title>Cobalt Ember Studios – Playing Card Box Dieline</title>
<link rel="stylesheet" href="https://fonts.googleapis.com/css2?family=Teko:wght@400;500;600&family=Kaushan+Script&display=swap">
<style>
  :root {
    --backdrop-light: #f4f5f6;
    --backdrop-dark: #dfe1e3;
    --gold-deep: #b8902f;
    --gold-mid: #e2c565;
    --gold-light: #f7e9a4;
    --ink: #0b0b0c;
    --ink-soft: #1c1c1f;
    --cut-line: #e4007c;
    --chip-orange: #f7a51c;
  }
  html, body {
    margin: 0;
    padding: 0;
    width: 1200px;
    height: 716px;
    overflow: hidden;
  }
  body {
    background: radial-gradient(ellipse at center, var(--backdrop-light) 0%, var(--backdrop-dark) 100%);
  }
  .dieline {
    display: block;
    width: 1200px;
    height: 716px;
  }
  .cut { fill: none; stroke: var(--cut-line); stroke-width: 1; }
  .fold { fill: none; stroke: var(--cut-line); stroke-width: 0.8; stroke-dasharray: 3 2; }
  .foil { fill: url(#foil); }
  .ink { fill: var(--ink); }
  .foil-frame { fill: var(--ink); stroke: url(#foil); stroke-width: 3; }
  .side-wordmark {
    font-family: "Teko", "Arial Narrow", sans-serif;
    font-weight: 600;
    font-size: 62px;
    letter-spacing: 2px;
    fill: var(--gold-mid);
  }
  .brand-name {
    font-family: "Teko", "Arial Narrow", sans-serif;
    font-weight: 600;
    font-size: 28px;
    letter-spacing: 0.5px;
    fill: var(--chip-orange);
  }
  .title-script {
    font-family: "Kaushan Script", cursive;
    font-size: 36px;
    fill: var(--gold-mid);
  }
  .edition {
    font-family: "Teko", "Arial Narrow", sans-serif;
    font-weight: 500;
    font-size: 21px;
    fill: var(--gold-mid);
  }
  .legal {
    font-family: "Teko", "Arial Narrow", sans-serif;
    font-weight: 400;
    font-size: 15px;
    fill: var(--gold-mid);
  }
  .suits {
    font-family: "Teko", "Arial Narrow", sans-serif;
    font-size: 14px;
    fill: var(--gold-mid);
  }
</style>
</head>
<body>
<svg class="dieline" viewBox="0 0 1200 716" xmlns="http://www.w3.org/2000/svg">
  <defs>
    <linearGradient id="foil" x1="0" y1="0" x2="1" y2="1">
      <stop offset="0" stop-color="#d8b957"/>
      <stop offset="0.35" stop-color="#f7e9a4"/>
      <stop offset="0.65" stop-color="#e2c565"/>
      <stop offset="1" stop-color="#b8902f"/>
    </linearGradient>
    <linearGradient id="night-scene" x1="0" y1="0" x2="0" y2="1">
      <stop offset="0" stop-color="#0a0f1e"/>
      <stop offset="0.45" stop-color="#3a2d1c"/>
      <stop offset="0.7" stop-color="#b8893a"/>
      <stop offset="1" stop-color="#0f2340"/>
    </linearGradient>
    <radialGradient id="quilt-back" cx="0.5" cy="0.5" r="0.7">
      <stop offset="0" stop-color="#2a2a2e"/>
      <stop offset="1" stop-color="#0e0e10"/>
    </radialGradient>
    <linearGradient id="glue-fade" x1="0" y1="0" x2="0" y2="1">
      <stop offset="0" stop-color="#e2c565"/>
      <stop offset="0.45" stop-color="#0b0b0c"/>
    </linearGradient>
  </defs>

  <!-- Left side panel -->
  <g class="side-panel side-panel--left">
    <polygon class="foil" points="218,165 232,130 294,130 294,604 218,604"/>
    <polygon class="ink" points="218,604 294,604 294,630 280,638 280,664 232,664 232,638 218,630"/>
    <polygon class="cut" points="218,165 232,130 294,130 294,604 294,630 280,638 280,664 232,664 232,638 218,630"/>
    <line class="fold" x1="218" y1="198" x2="294" y2="198"/>
    <line class="fold" x1="218" y1="604" x2="294" y2="604"/>
    <rect class="foil-frame" x="226" y="210" width="60" height="386" rx="6"/>
    <text class="side-wordmark" transform="translate(240 403) rotate(90)" text-anchor="middle">COBALT EMBER</text>
  </g>

  <!-- Front panel with tuck flap -->
  <g class="front-panel">
    <path class="foil" d="M298,116 L298,100 Q298,32 441,30 Q584,32 586,100 L586,116 Z"/>
    <rect class="foil" x="294" y="116" width="294" height="82"/>
    <rect class="foil" x="294" y="198" width="294" height="406"/>
    <path class="cut" d="M294,198 L294,116 L330,116 L330,120 M552,120 L552,116 L588,116 L588,198 M298,116 L298,100 Q298,32 441,30 Q584,32 586,100 L586,116"/>
    <line class="fold" x1="330" y1="120" x2="552" y2="120"/>
    <line class="fold" x1="294" y1="198" x2="588" y2="198"/>
    <rect class="foil-frame" x="305" y="209" width="272" height="388" rx="6"/>
    <line class="fold" x1="306" y1="248" x2="576" y2="248"/>

    <g class="brand-lockup">
      <circle cx="441" cy="306" r="58" fill="var(--ink-soft)"/>
      <text class="brand-name" x="441" y="315" text-anchor="middle">COBALT EMBER STUDIOS</text>
    </g>

    <text class="title-script" x="441" y="418" text-anchor="middle">Playing Cards</text>
    <text class="edition" x="441" y="450" text-anchor="middle">Premium Edition</text>

    <rect x="307" y="462" width="268" height="133" fill="url(#night-scene)" role="img" aria-label="Night skyline photograph with the Kelverin Arch and Moss Pavilion, lit fountains in the foreground"/>

    <rect class="ink" x="296" y="604" width="290" height="80"/>
    <polygon class="cut" points="294,604 296,604 296,684 586,684 586,604 588,604"/>
    <line class="fold" x1="294" y1="604" x2="588" y2="604"/>
  </g>

  <!-- Middle side panel -->
  <g class="side-panel side-panel--middle">
    <polygon class="foil" points="588,130 656,130 670,165 670,604 588,604"/>
    <polygon class="ink" points="588,604 670,604 670,630 656,638 656,664 604,664 604,638 588,630"/>
    <polygon class="cut" points="588,130 656,130 670,165 670,630 656,638 656,664 604,664 604,638 588,630"/>
    <line class="fold" x1="588" y1="198" x2="670" y2="198"/>
    <line class="fold" x1="588" y1="604" x2="670" y2="604"/>
    <rect class="foil-frame" x="597" y="210" width="64" height="386" rx="6"/>
    <text class="side-wordmark" transform="translate(612 403) rotate(90)" text-anchor="middle">COBALT EMBER</text>
  </g>

  <!-- Back panel -->
  <g class="back-panel">
    <path class="foil" d="M670,198 L774,198 A44,44 0 0 0 858,198 L960,198 L960,604 L670,604 Z"/>
    <path class="cut" d="M670,198 L774,198 A44,44 0 0 0 858,198 L960,198"/>
    <rect class="ink" x="676" y="208" width="278" height="392"/>
    <rect x="679" y="216" width="272" height="372" rx="8" fill="url(#quilt-back)" stroke="url(#foil)" stroke-width="3" role="img" aria-label="Quilted diamond pattern with card suit motifs"/>

    <g class="brand-lockup">
      <circle cx="816" cy="400" r="62" fill="var(--ink-soft)"/>
      <text class="brand-name" x="816" y="409" text-anchor="middle">COBALT EMBER STUDIOS</text>
    </g>

    <rect class="ink" x="670" y="604" width="290" height="82"/>
    <polyline class="cut" points="670,604 670,686 958,686 960,604"/>
    <line class="fold" x1="670" y1="604" x2="960" y2="604"/>
    <text class="legal" x="816" y="633" text-anchor="middle">Copyright 2021 Cobalt Ember Studios,</text>
    <text class="legal" x="816" y="651" text-anchor="middle">Marlow Bay, Westerland, Printed by RWLT</text>
    <text class="suits" x="816" y="670" text-anchor="middle" letter-spacing="8">♥♣♦♠</text>
  </g>

  <!-- Glue flap -->
  <g class="glue-flap">
    <polygon points="960,198 1030,214 1032,584 960,600" fill="url(#glue-fade)"/>
    <polygon class="cut" points="960,198 1030,214 1032,584 960,600"/>
    <line class="fold" x1="960" y1="198" x2="960" y2="604"/>
  </g>
</svg>
</body>
</html>
```